Flyer design for webdesign company

create a flyer that can be printed or sent as an email. The flyer needs to be professional, modern and engaging.

Reason: opportunity for all designers to get their designs in.

Target Market(s)

business owners that do not have a website

Industry/Entity Type

It Company

Font styles to use
Sans Serif

```html
<!DOCTYPE html>
<html lang="en">
<head>
<meta charset="utf-8">
<title>novasites – Dry Cleaning Websites Flyer</title>
<link rel="stylesheet" href="https://fonts.googleapis.com/css2?family=Roboto:wght@300;400;700&family=Roboto+Condensed:wght@700&display=swap">
<style>
  :root {
    --orange: #ec8a2d;
    --orange-dark: #d9761c;
    --orange-soft: #f3ad6a;
    --grey-dark: #5f5f5f;
    --grey-text: #767676;
    --paper: #ffffff;
    --backdrop: #ece9e6;
  }
  * { margin: 0; padding: 0; box-sizing: border-box; }
  html, body {
    width: 1041px;
    height: 1200px;
    overflow: hidden;
    background: var(--backdrop);
  }
  .flyer {
    position: absolute;
    left: 70px;
    top: 19px;
    width: 838px;
    height: 1082px;
    background: var(--paper);
    transform: scale(1.074);
    transform-origin: top left;
    font-family: 'Roboto', Arial, sans-serif;
    color: var(--grey-text);
  }

  /* Brand */
  .brand {
    position: absolute;
    left: 44px;
    top: 40px;
    width: 200px;
    height: 180px;
  }
  .brand-mark {
    position: absolute;
    left: 60px;
    top: 20px;
    width: 80px;
    height: 80px;
    border-radius: 50%;
    background: var(--orange);
  }
  .brand-name {
    position: absolute;
    left: 0;
    top: 138px;
    width: 200px;
    text-align: center;
    font-size: 30px;
    font-weight: 400;
    color: var(--grey-dark);
  }

  /* Contact */
  .contact {
    position: absolute;
    left: 262px;
    top: 68px;
    font-weight: 700;
    font-size: 23px;
    line-height: 29px;
    color: var(--grey-dark);
  }

  .headline {
    position: absolute;
    left: 258px;
    top: 132px;
    font-family: 'Roboto Condensed', 'Arial Narrow', sans-serif;
    font-weight: 700;
    font-size: 46px;
    line-height: 38px;
    color: var(--orange);
    text-transform: uppercase;
  }

  /* Hero */
  .hero {
    position: absolute;
    left: 45px;
    top: 232px;
    width: 745px;
    height: 349px;
    border-radius: 4px;
    overflow: hidden;
    background: linear-gradient(100deg, #dcdde4 0%, #eeeef0 35%, #c9c6d6 62%, #7b68b0 78%, #4c4f6e 100%);
  }
  .hero-title {
    position: absolute;
    left: 68px;
    top: 412px;
    font-family: 'Roboto Condensed', 'Arial Narrow', sans-serif;
    font-weight: 700;
    font-size: 76px;
    line-height: 66px;
    color: var(--orange);
    text-transform: uppercase;
    text-shadow: 0 0 3px #fff, 0 0 3px #fff, 0 0 6px #fff, 0 0 8px #fff;
  }

  .price-badge {
    position: absolute;
    left: 621px;
    top: 235px;
    width: 210px;
    height: 210px;
    border-radius: 50%;
    background: var(--orange);
    border: 7px solid var(--orange-soft);
    display: flex;
    align-items: center;
    justify-content: center;
    text-align: center;
    font-family: 'Roboto Condensed', 'Arial Narrow', sans-serif;
    font-weight: 700;
    font-size: 44px;
    line-height: 40px;
    color: #fff;
    text-transform: uppercase;
  }

  /* Benefits */
  .benefits {
    position: absolute;
    left: 46px;
    top: 598px;
    width: 780px;
    list-style: none;
  }
  .benefit {
    position: absolute;
    display: flex;
    align-items: flex-start;
  }
  .benefit-tick {
    flex: none;
    width: 73px;
    height: 67px;
  }
  .benefit-text {
    margin-left: 18px;
    font-size: 17.5px;
    line-height: 22.5px;
    font-weight: 300;
    color: var(--grey-text);
    width: 290px;
  }
  .benefit-text strong { font-weight: 700; }
  .col-left { left: 0; }
  .col-right { left: 385px; }
  .row-1 { top: 0; }
  .row-2 { top: 85px; }
  .row-3 { top: 170px; }
  .row-4 { top: 255px; }

  /* Footer band */
  .offer-band {
    position: absolute;
    left: 0;
    top: 930px;
    width: 838px;
    height: 152px;
    background: var(--orange);
    color: #fff;
    text-align: center;
  }
  .offer-note {
    margin-top: 8px;
    font-weight: 700;
    font-size: 23px;
    line-height: 29px;
  }
  .offer-price {
    font-family: 'Roboto Condensed', 'Arial Narrow', sans-serif;
    font-weight: 700;
    font-size: 42px;
    line-height: 38px;
    text-transform: uppercase;
    text-shadow: 0 0 3px rgba(255,255,255,0.6);
  }
</style>
</head>
<body>
  <main class="flyer">
    <div class="brand">
      <span class="brand-mark"></span>
      <span class="brand-name">novasites</span>
    </div>

    <div class="contact">
      <p>Call Today 1-800-555-0142</p>
      <p>www.novasites-web.com</p>
    </div>

    <h1 class="headline">Attract more customers<br>Make more money</h1>

    <div class="hero" role="img" aria-label="Photo of a smiling dry cleaner at her counter with folded shirts and hanging garments"></div>
    <h2 class="hero-title">Dry cleaning<br>websites</h2>

    <div class="price-badge">Only<br>3 $<br>a day!</div>

    <ul class="benefits">
      <li class="benefit col-left row-1">
        <svg class="benefit-tick" viewBox="0 0 73 67" aria-hidden="true"><rect x="1" y="1" width="71" height="65" rx="4" fill="var(--orange)" stroke="var(--orange-dark)" stroke-width="2"/><path d="M16 35 L30 49 L58 19" fill="none" stroke="#fff" stroke-width="9" stroke-linecap="round" stroke-linejoin="round"/></svg>
        <p class="benefit-text"><strong>97%</strong> of people look online for businesses.<br>You need a website!</p>
      </li>
      <li class="benefit col-left row-2">
        <svg class="benefit-tick" viewBox="0 0 73 67" aria-hidden="true"><rect x="1" y="1" width="71" height="65" rx="4" fill="var(--orange)" stroke="var(--orange-dark)" stroke-width="2"/><path d="M16 35 L30 49 L58 19" fill="none" stroke="#fff" stroke-width="9" stroke-linecap="round" stroke-linejoin="round"/></svg>
        <p class="benefit-text" style="margin-top:12px"><strong>You're losing many customers by not having a website</strong></p>
      </li>
      <li class="benefit col-left row-3">
        <svg class="benefit-tick" viewBox="0 0 73 67" aria-hidden="true"><rect x="1" y="1" width="71" height="65" rx="4" fill="var(--orange)" stroke="var(--orange-dark)" stroke-width="2"/><path d="M16 35 L30 49 L58 19" fill="none" stroke="#fff" stroke-width="9" stroke-linecap="round" stroke-linejoin="round"/></svg>
        <p class="benefit-text" style="margin-top:10px">Beat your competition with better visibility and credibility</p>
      </li>
      <li class="benefit col-left row-4">
        <svg class="benefit-tick" viewBox="0 0 73 67" aria-hidden="true"><rect x="1" y="1" width="71" height="65" rx="4" fill="var(--orange)" stroke="var(--orange-dark)" stroke-width="2"/><path d="M16 35 L30 49 L58 19" fill="none" stroke="#fff" stroke-width="9" stroke-linecap="round" stroke-linejoin="round"/></svg>
        <p class="benefit-text" style="margin-top:10px"><strong>BEAUTIFUL WEBSITES</strong><br>AVAILABLE NOW</p>
      </li>
      <li class="benefit col-right row-1">
        <svg class="benefit-tick" viewBox="0 0 73 67" aria-hidden="true"><rect x="1" y="1" width="71" height="65" rx="4" fill="var(--orange)" stroke="var(--orange-dark)" stroke-width="2"/><path d="M16 35 L30 49 L58 19" fill="none" stroke="#fff" stroke-width="9" stroke-linecap="round" stroke-linejoin="round"/></svg>
        <p class="benefit-text" style="margin-top:10px">Smart, clean website designs<br><strong>($3000 Value. No extra charge)</strong></p>
      </li>
      <li class="benefit col-right row-2">
        <svg class="benefit-tick" viewBox="0 0 73 67" aria-hidden="true"><rect x="1" y="1" width="71" height="65" rx="4" fill="var(--orange)" stroke="var(--orange-dark)" stroke-width="2"/><path d="M16 35 L30 49 L58 19" fill="none" stroke="#fff" stroke-width="9" stroke-linecap="round" stroke-linejoin="round"/></svg>
        <p class="benefit-text" style="margin-top:8px">Limited to ONLY 4 WEBSITES per area. Don't miss out!</p>
      </li>
      <li class="benefit col-right row-3">
        <svg class="benefit-tick" viewBox="0 0 73 67" aria-hidden="true"><rect x="1" y="1" width="71" height="65" rx="4" fill="var(--orange)" stroke="var(--orange-dark)" stroke-width="2"/><path d="M16 35 L30 49 L58 19" fill="none" stroke="#fff" stroke-width="9" stroke-linecap="round" stroke-linejoin="round"/></svg>
        <p class="benefit-text" style="margin-top:4px">Social Media setup options<br>(search &amp; social profiles)</p>
      </li>
    </ul>

    <section class="offer-band">
      <p class="offer-note">Stop wasting money on mailers and<br>print advertising.</p>
      <p class="offer-price">Pricing:<br>Only $99/month</p>
    </section>
  </main>
</body>
</html>
```